Copper wren builds

Copper wren builds is a small construction company.
Who is a licenced builder, Carpenter, joiner,
working on heritage ,new build, speacial projects and sometimes furniture

Industry/Entity Type

Construction

```html
<!DOCTYPE html>
<html lang="en">
<head>
<meta charset="utf-8">
<title>Copper wren builds – Business Card</title>
<link rel="stylesheet" href="https://fonts.googleapis.com/css2?family=Open+Sans:wght@400&family=Oxygen:wght@400&family=Quicksand:wght@700&family=Ubuntu:ital,wght@1,300&display=swap">
<style>
  :root {
    --backdrop: #e9e7e3;
    --card: #231f20;
    --green: #137a3c;
    --green-soft: #106b34;
  }
  html, body {
    margin: 0;
    width: 1200px;
    height: 1200px;
    overflow: hidden;
    background: var(--backdrop);
  }
  .business-card {
    position: absolute;
    left: 50px;
    top: 286px;
    width: 1100px;
    height: 628px;
    display: block;
  }
  .card-face { fill: var(--card); }
  .edge-band { fill: var(--green); }
  .company-name {
    font-family: "Oxygen", sans-serif;
    font-size: 70px;
    fill: var(--green);
  }
  .owner-name {
    font-family: "Quicksand", sans-serif;
    font-weight: 700;
    font-size: 74px;
    fill: var(--green);
  }
  .owner-role {
    font-family: "Ubuntu", sans-serif;
    font-style: italic;
    font-weight: 300;
    font-size: 40px;
    fill: var(--green);
  }
  .phone-number {
    font-family: "Oxygen", sans-serif;
    font-size: 58px;
    fill: var(--green-soft);
  }
  .phone-icon {
    fill: none;
    stroke: var(--green-soft);
    stroke-width: 3;
  }
  .services-title,
  .service-item {
    font-family: "Open Sans", sans-serif;
    fill: var(--green-soft);
  }
  .services-title { font-size: 25px; }
  .service-item { font-size: 25px; }
</style>
</head>
<body>
<svg class="business-card" viewBox="0 0 1100 628" xmlns="http://www.w3.org/2000/svg" role="img" aria-label="Copper wren builds business card for Marcus Hale">
  <rect class="card-face" x="0" y="0" width="1100" height="628"/>

  <path class="edge-band" d="M0,42 C30,52 32,88 32,112 L32,516 C32,542 30,572 0,586 Z"/>
  <path class="edge-band" d="M1100,42 C1070,52 1068,88 1068,112 L1068,516 C1068,542 1070,572 1100,586 Z"/>

  <text class="company-name" text-anchor="middle">
    <tspan x="205" y="209">Copper</tspan>
    <tspan x="205" y="297">wren</tspan>
    <tspan x="205" y="384">builds</tspan>
  </text>

  <text class="owner-name" x="980" y="115" text-anchor="end">Marcus Hale</text>
  <text class="owner-role" x="982" y="148" text-anchor="end">Owner</text>

  <g class="phone-icon">
    <rect x="527" y="210" width="28" height="52" rx="5"/>
    <line x1="527" y1="220" x2="555" y2="220"/>
    <line x1="527" y1="251" x2="555" y2="251"/>
    <circle cx="541" cy="256.5" r="2"/>
  </g>
  <text class="phone-number" x="591" y="256">0491570156</text>

  <text class="services-title" x="421" y="330">Services</text>
  <text class="service-item" x="413" y="386">- Licensed builder</text>
  <text class="service-item" x="413" y="443">- Carpenter</text>
  <text class="service-item" x="413" y="502">- Joiner</text>
  <text class="service-item" x="413" y="561">- New Build</text>

  <text class="service-item" x="750" y="386">- Special Projects</text>
  <text class="service-item" x="750" y="443">- Furniture</text>
  <text class="service-item" x="750" y="502">- Working On Heritage</text>
</svg>
</body>
</html>
```